Web Design for an Online Dating Web Site

We need an uncoded web design for a new online dating web site called pLirvo.com. Simplicity and boldness are the key factors in the successful design.
Please look at the requirements document attached for details.
Updates
Dear all,
Please AVOID USING A PICTURE OF A HAPPY COUPLE ON THE HOME PAGE of the site. We highly want to move away from this space as it makes our web site just like another dating web site.
We like something simple with web 2.0 look and feel. The examples in the Requirements Document are exactly the design we are after.
Regards
Tarn
Industry/Entity Type
Dating
Look and feel
Each slider illustrates characteristics of the customer's brand and the style your logo design should communicate.

```html
<!DOCTYPE html>
<html lang="en">
<head>
<meta charset="utf-8">
<title>pLirvo – Meet people unexpectedly</title>
<link rel="stylesheet" href="https://fonts.googleapis.com/css2?family=PT+Sans+Narrow:wght@400;700&family=Open+Sans:wght@400;600&display=swap">
<style>
:root{
  --berry:#a8203f;
  --berry-light:#bf3558;
  --berry-dark:#8a1a33;
  --pink:#f0238c;
  --pink-soft:#f58ab8;
  --white:#ffffff;
  --ink:#222222;
  --lime:#a6d61e;
  --lime-dark:#86b80e;
  --teal:#3fb3c8;
  --teal-dark:#2a95ab;
  --footer:#3b3b3b;
  --footer-dark:#2c2c2c;
  --muted:#cfcfcf;
}
*{box-sizing:border-box;margin:0;padding:0}
html,body{width:1200px;height:927px;overflow:hidden}
body{position:relative;font-family:"PT Sans Narrow",sans-serif;color:var(--white);
  background:radial-gradient(ellipse at 45% 35%,var(--berry-light) 0%,var(--berry) 55%,var(--berry-dark) 100%)}
.abs{position:absolute}
.top-strip{left:0;top:0;width:1200px;height:18px;background:var(--berry-dark)}
.brand{left:190px;top:28px;display:flex;align-items:center;gap:10px}
.brand-mark{width:22px;height:22px;border-radius:50%;background:var(--pink)}
.brand-name{font-family:"PT Sans Narrow",sans-serif;font-weight:700;font-size:62px;line-height:1;color:var(--pink)}
.nav{left:620px;top:34px;width:400px;height:70px}
.nav-item{position:absolute;top:0;width:80px;text-align:center;font-weight:700;font-size:17px;color:var(--white)}
.nav-item svg{display:block;margin:0 auto 8px;height:36px}
.nav-item.is-current{color:var(--pink-soft)}
.nav-dots{position:absolute;top:14px;font-size:0}
.nav-dots i{display:inline-block;width:6px;height:6px;border-radius:50%;background:rgba(255,255,255,.45);margin-right:4px}
.rule{left:186px;top:118px;width:827px;height:1px;background:rgba(255,255,255,.3)}
.intro{left:190px;top:138px;width:840px;font-weight:700;font-size:26px;letter-spacing:-.3px;line-height:32px;text-shadow:0 1px 2px rgba(0,0,0,.35)}
.slider-arrow{width:38px;height:38px;border-radius:50%;background:rgba(255,255,255,.75);top:297px}
.slider-arrow svg{display:block;margin:10px auto}
.slide{top:252px;width:235px;height:130px;background:var(--white);padding:4px;box-shadow:0 8px 10px -6px rgba(0,0,0,.5)}
.slide-art{width:100%;height:100%;position:relative;overflow:hidden}
.slide-caption{position:absolute;left:0;right:0;bottom:0;height:24px;background:rgba(255,235,225,.85);
  color:var(--ink);font-weight:700;font-size:16px;line-height:24px;text-align:center}
.clouds{left:0;top:480px;width:1200px;height:300px}
.section-title{font-weight:700;font-size:30px;text-shadow:0 1px 2px rgba(0,0,0,.3)}
.video{left:186px;top:471px;width:486px;height:263px;background:#000}
.play{left:399px;top:565px}
.login{left:690px;top:470px;width:323px;height:142px;background:var(--white);border-radius:6px;overflow:hidden;box-shadow:0 0 0 2px rgba(255,255,255,.4)}
.field{position:absolute;left:11px;width:170px;height:32px;border:1px solid #cfcfcf;border-radius:2px;
  box-shadow:inset 0 1px 3px rgba(0,0,0,.15);font-family:"Open Sans",sans-serif;font-size:12px;color:var(--ink);padding:0 11px;line-height:30px}
.forgot{position:absolute;left:209px;top:22px;font-family:"Open Sans",sans-serif;font-size:12px;color:var(--ink);text-decoration:underline}
.signin-btn{position:absolute;left:201px;top:56px;width:105px;height:24px;border-radius:12px;
  background:linear-gradient(#c6ea4a,var(--lime));font-family:"Open Sans",sans-serif;font-size:12px;color:var(--white);line-height:24px;padding-left:24px}
.signin-btn b{position:absolute;right:0;top:0;width:18px;height:24px;border-radius:0 12px 12px 0;background:var(--lime-dark)}
.signin-btn b::after{content:"";position:absolute;left:6px;top:8px;border-left:6px solid #1d3b00;border-top:4px solid transparent;border-bottom:4px solid transparent}
.alt-login{position:absolute;left:0;right:0;bottom:0;height:47px;background:linear-gradient(var(--lime),var(--lime-dark));
  display:flex;align-items:center;padding-left:20px;gap:14px}
.alt-login .or{font-weight:700;font-size:26px;margin-right:8px}
.alt-login .dot{width:24px;height:24px;border-radius:50%;background:var(--white);box-shadow:inset 0 0 0 5px rgba(0,0,0,.12)}
.alt-login .more{font-weight:700;font-size:17px;margin-left:4px}
.signup{left:690px;top:633px;width:323px;height:103px;border-radius:6px;background:var(--white);padding:3px;box-shadow:0 0 3px rgba(0,0,0,.25)}
.signup span{display:block;height:100%;border-radius:4px;background:linear-gradient(#5ec6d8,var(--teal) 55%,var(--teal-dark));
  text-align:center;font-weight:700;font-size:50px;line-height:97px;text-shadow:0 2px 2px rgba(0,0,0,.3)}
.footer{left:0;top:774px;width:1200px;height:153px;background:linear-gradient(var(--footer),var(--footer-dark))}
.footer-title{left:187px;top:789px;font-weight:700;font-size:22px;color:#e8334f}
.footer-links{left:186px;top:815px;display:flex;gap:12px;font-weight:700;font-size:14px;color:var(--white)}
.footer-links span::before{content:"→ ";color:#e8334f}
.social{left:188px;top:845px;display:grid;grid-template-columns:repeat(5,33px);gap:5px 11px}
.social i{width:33px;height:33px;border-radius:5px;display:block}
.copyright{right:187px;top:803px;font-family:"Open Sans",sans-serif;font-size:12px;color:var(--white)}
.copyright em{font-style:normal;color:var(--pink)}
.footer-brand{right:187px;top:826px;font-weight:700;font-size:46px;line-height:1;color:var(--muted)}
.legal{right:187px;top:887px;font-family:"Open Sans",sans-serif;font-size:12px;color:var(--white)}
</style>
</head>
<body>
<div class="abs top-strip"></div>

<header>
  <div class="abs brand"><span class="brand-name">pLirvo</span><span class="brand-mark"></span></div>
  <nav class="abs nav">
    <div class="nav-item is-current" style="left:0">
      <svg viewBox="0 0 24 36" width="24"><text x="12" y="32" text-anchor="middle" font-family="PT Sans Narrow" font-weight="700" font-size="40" fill="#f58ab8">?</text></svg>Why</div>
    <div class="nav-dots" style="left:78px"><i></i><i></i><i></i></div>
    <div class="nav-item" style="left:110px">
      <svg viewBox="0 0 36 36" width="36"><g fill="#fff"><circle cx="22" cy="14" r="9"/><circle cx="11" cy="25" r="7"/></g><circle cx="22" cy="14" r="3.5" fill="#b52b4d"/><circle cx="11" cy="25" r="2.5" fill="#b52b4d"/></svg>How It Works</div>
    <div class="nav-dots" style="left:190px"><i></i><i></i><i></i></div>
    <div class="nav-item" style="left:218px">
      <svg viewBox="0 0 36 36" width="36"><rect x="7" y="8" width="22" height="15" rx="1" fill="none" stroke="#fff" stroke-width="3"/><rect x="3" y="25" width="30" height="3" fill="#fff"/></svg>Sign Up</div>
    <div class="nav-dots" style="left:300px"><i></i><i></i><i></i></div>
    <div class="nav-item" style="left:330px">
      <svg viewBox="0 0 36 36" width="36"><circle cx="10" cy="27" r="3.5" fill="#fff"/><path d="M7 17a12 12 0 0 1 12 12M7 8a21 21 0 0 1 21 21" fill="none" stroke="#fff" stroke-width="4"/></svg>Our Blog</div>
  </nav>
  <div class="abs rule"></div>
  <p class="abs intro">pLirvo provides a new and different way to meet people online that replicates the way you meet people in the real world, which more often that not is unexpectedly.</p>
</header>

<section class="slider">
  <div class="abs slider-arrow" style="left:169px"><svg width="12" height="18" viewBox="0 0 12 18"><path d="M10 2 3 9l7 7" fill="none" stroke="#222" stroke-width="3.5"/></svg></div>
  <div class="abs slide" style="left:213px"><div class="slide-art" role="img" aria-label="Silhouetted couple forming a heart against a sunset" style="background:linear-gradient(#b85a10,#f0a020 60%,#f7c35a)"><span class="slide-caption">Connections that just click</span></div></div>
  <div class="abs slide" style="left:482px"><div class="slide-art" role="img" aria-label="Man and woman seated on a sofa against a red wall" style="background:linear-gradient(#e0484f,#d73c44 65%,#e9e1d8 66%)"><span class="slide-caption">It comes when you least expect it.</span></div></div>
  <div class="abs slide" style="left:752px"><div class="slide-art" role="img" aria-label="Illustrated couple sharing wine at a table" style="background:linear-gradient(90deg,#ffffff,#f7d3de 50%,#ffffff)"><span class="slide-caption">It hides where you rarely look.</span></div></div>
  <div class="abs slider-arrow" style="left:993px"><svg width="12" height="18" viewBox="0 0 12 18"><path d="M2 2l7 7-7 7" fill="none" stroke="#222" stroke-width="3.5"/></svg></div>
</section>

<svg class="abs clouds" viewBox="0 0 1200 300" aria-hidden="true">
  <path fill="#fff" d="M0 18C20 4 45 4 60 18C80 0 115 2 130 22C150 8 175 12 190 26V300H0Z"/>
  <path fill="#fff" d="M672 22C690 8 705 10 720 26V300H672Z"/>
  <path fill="#fff" d="M1013 26C1030 6 1060 4 1080 20C1100 2 1140 4 1155 20C1170 8 1190 8 1200 16V300H1013Z"/>
  <rect x="672" y="60" width="345" height="240" fill="#fff"/>
  <rect x="0" y="150" width="1200" height="150" fill="#fff"/>
</svg>

<main>
  <h2 class="abs section-title" style="left:186px;top:430px">Want To Know How It Works?</h2>
  <div class="abs video"></div>
  <svg class="abs play" width="62" height="62" viewBox="0 0 62 62" aria-label="Play video"><circle cx="31" cy="31" r="28" fill="#333" stroke="#999" stroke-width="3"/><path d="M24 18v26l21-13z" fill="#ddd"/></svg>

  <h2 class="abs section-title" style="left:690px;top:432px;font-size:27px">Already a Member? Sign-In Now</h2>
  <form class="abs login">
    <div class="field" style="top:13px">User Name</div>
    <div class="field" style="top:52px">Password</div>
    <span class="forgot">Forgot Password?</span>
    <span class="signin-btn">SIGN-IN<b></b></span>
    <div class="alt-login"><span class="or">OR</span><i class="dot"></i><i class="dot"></i><i class="dot"></i><i class="dot"></i><i class="dot"></i><span class="more">More...</span></div>
  </form>
  <div class="abs signup"><span>SIGN UP NOW</span></div>
</main>

<footer class="abs footer"></footer>
<div class="abs footer-title">Read More</div>
<div class="abs footer-links"><span>Why pLirvo</span><span>How it works</span><span>Sign Up</span><span>Login</span><span>About Us</span></div>
<div class="abs social">
  <i style="background:#3b5a9a"></i><i style="background:#e8761e"></i><i style="background:#d4258f"></i><i style="background:#53b9e3"></i><i style="background:#1a74b0"></i>
  <i style="background:#e8e8e8"></i><i style="background:#6c8f2a"></i><i style="background:#e6e6e6"></i><i style="background:#d8233a"></i><i style="background:#f2f2f2"></i>
</div>
<div class="abs copyright">© 2011 <em>pLirvo</em> | All Rights Reserved</div>
<div class="abs footer-brand">pLirvo</div>
<div class="abs legal">Privacy Policy | Terms &amp; Conditions</div>
</body>
</html>
```